Product Label Design

Need a product design for our Epsom salt product, needs to have a luxurious simple feel to it. The picture attached is our brand and wordage on it, the bag we think should be a stand up bag that should be offwhite/creme color. The other picture are products that we like. We updated the packaging to be a Kraft tube box, please see the attached photo for dimensions.

```html
<!DOCTYPE html>
<html lang="en">
<head>
<meta charset="UTF-8">
<title>VELA Ascend – Epsom Salt Pouch Label</title>
<link rel="stylesheet" href="https://fonts.googleapis.com/css2?family=Montserrat:wght@500;700&family=Quicksand:wght@300;400&display=swap">
<style>
  :root {
    --backdrop: #86a9b3;
    --pouch: #fbfbf9;
    --ink: #3a3536;
    --teal-light: #45bfd8;
    --teal-deep: #1a94a9;
    --teal: #2fabc4;
  }
  * { margin: 0; padding: 0; box-sizing: border-box; }
  html, body {
    width: 1200px;
    height: 1128px;
    overflow: hidden;
    background: var(--backdrop);
  }
  .canvas {
    position: relative;
    width: 1200px;
    height: 1128px;
  }
  .label {
    position: absolute;
    left: 301px;
    top: 134px;
    width: 598px;
    height: 860px;
    background: var(--pouch);
    text-align: center;
  }
  .brand {
    position: absolute;
    top: 226px;
    left: 0;
    right: 0;
    font-family: "Montserrat", sans-serif;
    font-weight: 700;
    font-size: 44px;
    letter-spacing: 1px;
    color: var(--ink);
  }
  .product-name {
    position: absolute;
    top: 382px;
    left: 0;
    right: 0;
    font-family: "Quicksand", sans-serif;
    font-weight: 400;
    font-size: 52px;
    letter-spacing: 30px;
    padding-left: 30px;
    background: linear-gradient(90deg, var(--teal-light), var(--teal-deep));
    -webkit-background-clip: text;
    background-clip: text;
    color: transparent;
  }
  .descriptor {
    position: absolute;
    top: 524px;
    left: 0;
    right: 0;
    font-family: "Quicksand", sans-serif;
    font-weight: 400;
    font-size: 15px;
    line-height: 19px;
    letter-spacing: 1.5px;
    color: var(--ink);
  }
  .divider {
    position: absolute;
    top: 598px;
    left: 264px;
    width: 70px;
    height: 2px;
    background: var(--teal);
  }
  .botanicals {
    position: absolute;
    top: 642px;
    left: 0;
    right: 0;
    font-family: "Quicksand", sans-serif;
    font-weight: 300;
    font-size: 19px;
    line-height: 22px;
    letter-spacing: 2px;
    color: var(--teal);
  }
  .net-weight {
    position: absolute;
    top: 760px;
    left: 0;
    right: 0;
    font-family: "Montserrat", sans-serif;
    font-weight: 500;
    font-size: 11px;
    letter-spacing: 3px;
    color: var(--ink);
  }
</style>
</head>
<body>
  <main class="canvas">
    <section class="label">
      <h1 class="brand">VELA</h1>
      <h2 class="product-name">ASCEND</h2>
      <p class="descriptor">US Sourced Pure Epsom Salt<br>(Magnesium Sulfate)</p>
      <div class="divider"></div>
      <p class="botanicals">+ Abies sibirica<br>+ Fir Balsam</p>
      <p class="net-weight">NET WT. 3LBS (1360g)</p>
    </section>
  </main>
</body>
</html>
```